現在販売している商品(シリーズ商品)のデザイン変更を計画しております。
今回は表ラベルのデザインをお願い致します。

この商品は個食タイプの商品で現在は表ラベルを共通にして、4種類の味(たまり醤油・七味唐辛子・ねぎみそ・柚子こしょう)を販売しております。今後も入れ替えをしながらいろいろな味を販売していく予定です。

販売チャネルとしては、スーパーや企業売店などの米菓コーナーや個食コーナーです。

商品形態は、バラ詰めしたせんべい2枚を、無地袋に表ラベル(共通で使用)と味ラベルを貼付ます。(添付写真を参照)

商品の特徴として、
1.国産うるち米100%使用
2.それぞれの味で使用している調味料(しょうゆ・だし・香辛料)にもこだわりがある
3.一枚一枚に厚みがあり食べ応えがある本格派せんべい

商品サイズ:縦180m/m × 横140m/m
ラベルサイズ:縦85(±10)× 横40(±10)サイズ内での変形も可能
色数:3色程度で
紙質:和紙(雲龍)タイプを考えております。

シリーズものとして、制作して頂くラベルの脇に味ラベル(既存ラベル)を貼り付けます。

デザインイメージとしては、
品名は縦書き
和紙の風合いを活かし、シンプルで高級感をだす
ワンポイントとなるコピーやイラストを入れる

※現在使用しているラベルのコピー「伝統の味」は使わないでください。

大変選考に時間が掛かり申し訳ございません。
どのデザインも素晴らしく迷いましたが、
選考のポイントは、
①文字の見やすさ
②シンプルで分かりやすい
③全体のバランス
です。

この度は多数のご提案を頂きありがとうございました。
商品に特徴(ポイント)が無く、難しい案件かなと思っていましたが
思った以上に素晴らしいデザインで迷いました。
これからの皆様にご依頼することがあると思いますので
今後ともよろしくお願いいたします。

```html
<!DOCTYPE html>
<html lang="ja">
<head>
<meta charset="utf-8">
<title>せんべい 表ラベル</title>
<link href="https://fonts.googleapis.com/css2?family=Dela+Gothic+One&family=Zen+Old+Mincho:wght@700;900&display=swap" rel="stylesheet">
<style>
  :root {
    --ink: #111111;
    --paper: #ffffff;
    --grain: #ecd9b6;
    --grain-deep: #e2c89c;
    --seal: #c8262c;
  }
  html, body {
    margin: 0;
    padding: 0;
    width: 1200px;
    height: 2392px;
    overflow: hidden;
    background: var(--paper);
  }
  .label {
    position: relative;
    width: 1200px;
    height: 2392px;
  }
  .label-frame,
  .grain-art {
    position: absolute;
    left: 0;
    top: 0;
  }
  .catchphrase {
    position: absolute;
    left: 0;
    top: 215px;
    width: 1200px;
    margin: 0;
    text-align: center;
    font-family: "Zen Old Mincho", serif;
    font-weight: 900;
    font-size: 140px;
    line-height: 1;
    letter-spacing: 6px;
    color: var(--ink);
  }
  .header-rule {
    position: absolute;
    left: 40px;
    top: 384px;
    width: 1120px;
    height: 8px;
    background: var(--ink);
  }
  .product-name {
    position: absolute;
    left: 470px;
    top: 450px;
    margin: 0;
    writing-mode: vertical-rl;
    text-orientation: upright;
    font-family: "Dela Gothic One", sans-serif;
    font-weight: 400;
    font-size: 450px;
    line-height: 1;
    letter-spacing: -10px;
    color: var(--ink);
  }
  .feature-copy {
    position: absolute;
    left: 160px;
    top: 610px;
    margin: 0;
    writing-mode: vertical-rl;
    text-orientation: upright;
    font-family: "Zen Old Mincho", serif;
    font-weight: 700;
    font-size: 96px;
    line-height: 1;
    letter-spacing: 4px;
    color: var(--ink);
  }
  .seal {
    position: absolute;
    left: 176px;
    top: 2110px;
    width: 90px;
    height: 130px;
    border-radius: 16px;
    background: var(--seal);
  }
</style>
</head>
<body>
<div class="label">
  <svg class="grain-art" width="1200" height="2392" viewBox="0 0 1200 2392" role="img" aria-label="稲穂のイラスト（淡いベージュ）">
    <defs>
      <linearGradient id="grainTone" x1="0" y1="0" x2="0" y2="1">
        <stop offset="0" stop-color="var(--grain-deep)"/>
        <stop offset="1" stop-color="var(--grain)"/>
      </linearGradient>
    </defs>
    <path d="M420 420 C760 560 1080 1000 1080 1500 C1080 1900 900 2200 700 2340 L600 2340 C820 2150 980 1850 960 1480 C940 1060 700 680 420 520 Z" fill="url(#grainTone)" opacity="0.85"/>
  </svg>

  <svg class="label-frame" width="1200" height="2392" viewBox="0 0 1200 2392" aria-hidden="true">
    <path d="M100 32 H1100 A68 68 0 0 0 1168 100 V2292 A68 68 0 0 0 1100 2360 H100 A68 68 0 0 0 32 2292 V100 A68 68 0 0 0 100 32 Z"
          fill="none" stroke="var(--ink)" stroke-width="14"/>
  </svg>

  <h2 class="catchphrase">風味絶佳</h2>
  <div class="header-rule"></div>

  <h1 class="product-name">せんべい</h1>

  <p class="feature-copy">国産うるち米１００％使用</p>

  <div class="seal" role="img" aria-label="朱色の落款印"></div>
</div>
</body>
</html>
```